Marketing material for IT Company
Brochure/Sales Sheet/Flyer
Brochure will be in two languages, and tri-fold. Would go like this; front (outer) side: first fold: page for information in 2nd languge, second fold: page for information in 2nd language, third fold: cover page in 1st language; back side (inner) side: first fold is for information in 1st language, second fold is for information in 1st language, third fold is cover page for 2nd language.
Information Technology
Brochure view and dimensions are in an uploaded file. Size of flyer equals to size of 1 fold of brochure (i.e one brochure size = 3 flyers size). Size of Sales Sheet is equal to brochure's size. (Sales Sheet won't be folded).
Trifold Brochure view and dimensions
Tulmori logo and Divisions logos (CMYK)
Tulmori logo and Divisions logos (PMS)
Tulmori vertical logo and Divisions vertical logos (CMYK)
Tulmori vertical logo and Divisions vertical logos (PMS)
Tulmori old Brochure (uploaded as an example)
Example of our folder, if it can help
Example of our biz card, if it can help
To help you understand how we see our brochure, one more PIC
Tulmori logo colors information

```html
<!DOCTYPE html>
<html lang="en">
<head>
<meta charset="utf-8">
<title>Tulmori brochure and flyers</title>
<link href="https://fonts.googleapis.com/css2?family=Open+Sans:wght@400;600;700&display=swap" rel="stylesheet">
<style>
:root{
  --canvas:#d9d9d9;
  --paper:#ffffff;
  --ink:#4a4a4a;
  --ink-soft:#777777;
  --brand:#3d4a57;
  --red:#d9322b;
  --orange:#ef8a1f;
  --yellow:#f2c21a;
  --green:#5fae3c;
  --blue:#2f7fc2;
  --footer:#9a9a9a;
}
*{box-sizing:border-box;margin:0;padding:0}
html,body{width:1200px;height:835px;overflow:hidden;background:var(--canvas);font-family:"Open Sans",Arial,sans-serif;color:var(--ink)}
.stage{position:relative;width:1200px;height:835px}
.row{position:absolute;left:24px;width:1130px;height:372px}
.row-outer{top:24px}
.row-inner{top:420px}

/* brochure */
.brochure{position:absolute;left:0;top:0;width:544px;height:372px;display:flex;box-shadow:0 1px 3px rgba(0,0,0,.25)}
.panel{position:relative;width:181.33px;height:372px;background:var(--paper);overflow:hidden}
.panel-info{background:linear-gradient(160deg,#fbeef0 0%,#ffffff 45%,#eef6e8 100%)}
.panel-info-alt{background:linear-gradient(200deg,#eef3fa 0%,#ffffff 50%,#fdf3e4 100%)}
.photo{position:absolute}
.photo-office{left:0;top:0;width:100%;height:58px;background:linear-gradient(180deg,#c9b9a3,#8f8172)}
.portraits{position:absolute;left:10px;top:62px;display:flex;gap:6px}
.portrait{width:24px;height:24px;border-radius:50%;background:radial-gradient(circle at 50% 40%,#d9c4b0,#7c6b5d);border:2px solid #fff;box-shadow:0 0 0 1px #ccc}
.section{position:absolute;left:10px;right:10px}
.label{display:flex;align-items:center;gap:4px;font-size:7px;font-weight:700;color:var(--brand);margin-bottom:4px}
.dot{width:7px;height:7px;border-radius:50%}
.copy{font-size:4.6px;line-height:1.55;color:var(--ink-soft)}
.bullets{list-style:none;margin-top:4px}
.bullets li{font-size:4.6px;line-height:1.7;color:var(--ink-soft);padding-left:6px;position:relative}
.bullets li::before{content:"";position:absolute;left:0;top:2.3px;width:3px;height:3px;border-radius:50%;background:var(--accent,var(--green))}
.photo-hand{left:0;top:0;width:100%;height:150px;background:linear-gradient(160deg,#cfe4f6,#3d7fbf 70%,#1f4f86)}
.swoosh{position:absolute;left:0;width:100%}
.photo-cover{left:0;top:0;width:100%;height:170px;background:linear-gradient(200deg,#d6e8f8,#4a8ccc 65%,#234f84)}
.cover-mark{position:absolute;left:0;right:0;top:212px;display:flex;flex-direction:column;align-items:center;gap:10px}
.mark-circle{width:54px;height:54px;border-radius:50%;background:var(--orange)}
.cover-name{font-size:26px;font-weight:700;color:var(--brand);letter-spacing:.5px}
.web-bar{position:absolute;left:0;bottom:0;width:100%;height:12px;background:var(--footer);color:#fff;font-size:5px;text-align:center;line-height:12px;letter-spacing:.6px}

/* flyers */
.flyer{position:absolute;top:0;width:134px;height:372px;background:var(--paper);overflow:hidden;box-shadow:0 1px 3px rgba(0,0,0,.25)}
.flyer:nth-child(2){left:556px}
.flyer:nth-child(3){left:700px}
.flyer:nth-child(4){left:844px}
.flyer:nth-child(5){left:988px}
.flyer-logo{position:absolute;top:10px;left:0;right:0;display:flex;justify-content:center;align-items:center;gap:5px}
.flyer-logo .dot{width:13px;height:13px;background:var(--green)}
.flyer-logo span{font-size:15px;font-weight:700;color:var(--brand)}
.photo-team{left:0;top:36px;width:100%;height:112px;background:linear-gradient(180deg,#e4e7ea,#9aa3ab)}
.flyer .section{top:172px;left:9px;right:9px}
.flyer .label{font-size:7.5px}
.flyer .label .dot{background:var(--accent)}
</style>
</head>
<body>
<main class="stage">

  <!-- outer side -->
  <section class="row row-outer">
    <div class="brochure">
      <article class="panel panel-info">
        <div class="photo photo-office" role="img" aria-label="Office team photo"></div>
        <div class="portraits">
          <div class="portrait" role="img" aria-label="Staff portrait"></div>
          <div class="portrait" role="img" aria-label="Staff portrait"></div>
          <div class="portrait" role="img" aria-label="Staff portrait"></div>
          <div class="portrait" role="img" aria-label="Staff portrait"></div>
        </div>
        <div class="section" style="top:102px;--accent:var(--green)">
          <div class="label"><span class="dot" style="background:var(--green)"></span>tulmori labs</div>
          <p class="copy">We build secure networks, software and support services that help growing companies work faster every day.</p>
          <ul class="bullets"><li>Managed servers and cloud hosting</li><li>Round the clock helpdesk support</li></ul>
        </div>
        <div class="section" style="top:218px;--accent:var(--orange)">
          <div class="label"><span class="dot" style="background:var(--orange)"></span>tulmori services</div>
          <p class="copy">We build secure networks, software and support services that help growing companies work faster every day.</p>
          <ul class="bullets"><li>Managed servers and cloud hosting</li><li>Round the clock helpdesk support</li></ul>
        </div>
      </article>
      <article class="panel panel-info-alt">
        <div class="photo photo-hand" role="img" aria-label="Hand touching a digital screen"></div>
        <svg class="swoosh" style="top:120px" width="182" height="50" viewBox="0 0 182 50" aria-hidden="true">
          <path d="M0 30 Q90 0 182 18 L182 50 L0 50Z" fill="#fff"/>
          <path d="M0 30 Q90 0 182 18" fill="none" stroke="#5fae3c" stroke-width="2"/>
        </svg>
        <div class="section" style="top:172px;--accent:var(--blue)">
          <p class="copy">We build secure networks, software and support services that help growing companies work faster every day.</p>
          <ul class="bullets"><li>Managed servers and cloud hosting</li><li>Round the clock helpdesk support</li><li>Custom software for your team</li></ul>
        </div>
        <div class="section" style="top:268px;--accent:var(--blue)">
          <p class="copy">We build secure networks, software and support services that help growing companies work faster every day.</p>
          <ul class="bullets"><li>Managed servers and cloud hosting</li><li>Round the clock helpdesk support</li></ul>
        </div>
      </article>
      <article class="panel">
        <div class="photo photo-cover" role="img" aria-label="Hand pressing a glowing button"></div>
        <svg class="swoosh" style="top:130px" width="182" height="60" viewBox="0 0 182 60" aria-hidden="true">
          <path d="M0 40 Q100 5 182 25 L182 60 L0 60Z" fill="#fff"/>
          <path d="M0 40 Q100 5 182 25" fill="none" stroke="#dfe6ee" stroke-width="4"/>
        </svg>
        <div class="cover-mark"><div class="mark-circle"></div><div class="cover-name">tulmori</div></div>
        <div class="web-bar">www.lorvex.net</div>
      </article>
    </div>

    <article class="flyer" style="--accent:var(--red)">
      <div class="flyer-logo"><span class="dot"></span><span>tulmori</span></div>
      <div class="photo photo-team" role="img" aria-label="Two business people in an office"></div>
      <svg class="swoosh" style="top:128px" width="134" height="40" viewBox="0 0 134 40" aria-hidden="true"><path d="M0 26 Q70 0 134 12 L134 40 L0 40Z" fill="#fff"/><path d="M0 24 Q70 -2 134 10" fill="none" stroke="#d9322b" stroke-width="4"/><path d="M0 30 Q70 6 134 16" fill="none" stroke="#ef8a1f" stroke-width="2"/></svg>
      <div class="section"><div class="label"><span class="dot"></span>tulmori labs</div><p class="copy">We build secure networks, software and support services that help growing companies work faster every day.</p><ul class="bullets"><li>Managed servers and cloud hosting</li><li>Round the clock helpdesk support</li><li>Custom software for your team</li></ul></div>
      <div class="web-bar">www.lorvex.net</div>
    </article>
    <article class="flyer" style="--accent:var(--red)">
      <div class="flyer-logo"><span class="dot"></span><span>tulmori</span></div>
      <div class="photo photo-team" role="img" aria-label="Business man in an office"></div>
      <svg class="swoosh" style="top:128px" width="134" height="40" viewBox="0 0 134 40" aria-hidden="true"><path d="M0 26 Q70 0 134 12 L134 40 L0 40Z" fill="#fff"/><path d="M0 24 Q70 -2 134 10" fill="none" stroke="#d9322b" stroke-width="4"/></svg>
      <div class="section"><div class="label"><span class="dot"></span>tulmori labs</div><p class="copy">We build secure networks, software and support services that help growing companies work faster every day.</p><ul class="bullets"><li>Managed servers and cloud hosting</li><li>Round the clock helpdesk support</li><li>Custom software for your team</li></ul></div>
      <div class="web-bar">www.lorvex.net</div>
    </article>
    <article class="flyer" style="--accent:var(--yellow)">
      <div class="flyer-logo"><span class="dot"></span><span>tulmori</span></div>
      <div class="photo photo-team" role="img" aria-label="Support staff with headsets"></div>
      <svg class="swoosh" style="top:128px" width="134" height="40" viewBox="0 0 134 40" aria-hidden="true"><path d="M0 26 Q70 0 134 12 L134 40 L0 40Z" fill="#fff"/><path d="M0 24 Q70 -2 134 10" fill="none" stroke="#f2c21a" stroke-width="4"/></svg>
      <div class="section"><div class="label"><span class="dot"></span>tulmori services</div><p class="copy">We build secure networks, software and support services that help growing companies work faster every day.</p><ul class="bullets"><li>Managed servers and cloud hosting</li><li>Round the clock helpdesk support</li><li>Custom software for your team</li></ul></div>
      <div class="web-bar">www.lorvex.net</div>
    </article>
    <article class="flyer" style="--accent:var(--orange)">
      <div class="flyer-logo"><span class="dot"></span><span>tulmori</span></div>
      <div class="photo photo-team" role="img" aria-label="Support staff with headsets"></div>
      <svg class="swoosh" style="top:128px" width="134" height="40" viewBox="0 0 134 40" aria-hidden="true"><path d="M0 26 Q70 0 134 12 L134 40 L0 40Z" fill="#fff"/><path d="M0 24 Q70 -2 134 10" fill="none" stroke="#ef8a1f" stroke-width="4"/></svg>
      <div class="section"><div class="label"><span class="dot"></span>tulmori services</div><p class="copy">We build secure networks, software and support services that help growing companies work faster every day.</p><ul class="bullets"><li>Managed servers and cloud hosting</li><li>Round the clock helpdesk support</li><li>Custom software for your team</li></ul></div>
      <div class="web-bar">www.lorvex.net</div>
    </article>
  </section>

  <!-- inner side -->
  <section class="row row-inner">
    <div class="brochure">
      <article class="panel panel-info">
        <div class="photo photo-office" role="img" aria-label="Office team photo"></div>
        <div class="portraits">
          <div class="portrait" role="img" aria-label="Staff portrait"></div>
          <div class="portrait" role="img" aria-label="Staff portrait"></div>
          <div class="portrait" role="img" aria-label="Staff portrait"></div>
          <div class="portrait" role="img" aria-label="Staff portrait"></div>
        </div>
        <div class="section" style="top:102px;--accent:var(--green)">
          <div class="label"><span class="dot" style="background:var(--green)"></span>tulmori labs</div>
          <p class="copy">We build secure networks, software and support services that help growing companies work faster every day.</p>
          <ul class="bullets"><li>Managed servers and cloud hosting</li><li>Round the clock helpdesk support</li></ul>
        </div>
        <div class="section" style="top:218px;--accent:var(--orange)">
          <div class="label"><span class="dot" style="background:var(--orange)"></span>tulmori services</div>
          <p class="copy">We build secure networks, software and support services that help growing companies work faster every day.</p>
          <ul class="bullets"><li>Managed servers and cloud hosting</li><li>Round the clock helpdesk support</li></ul>
        </div>
      </article>
      <article class="panel panel-info-alt">
        <div class="photo photo-hand" role="img" aria-label="Hand touching a digital screen"></div>
        <svg class="swoosh" style="top:120px" width="182" height="50" viewBox="0 0 182 50" aria-hidden="true">
          <path d="M0 30 Q90 0 182 18 L182 50 L0 50Z" fill="#fff"/>
          <path d="M0 30 Q90 0 182 18" fill="none" stroke="#5fae3c" stroke-width="2"/>
        </svg>
        <div class="section" style="top:172px;--accent:var(--blue)">
          <p class="copy">We build secure networks, software and support services that help growing companies work faster every day.</p>
          <ul class="bullets"><li>Managed servers and cloud hosting</li><li>Round the clock helpdesk support</li><li>Custom software for your team</li></ul>
        </div>
        <div class="section" style="top:268px;--accent:var(--blue)">
          <p class="copy">We build secure networks, software and support services that help growing companies work faster every day.</p>
          <ul class="bullets"><li>Managed servers and cloud hosting</li><li>Round the clock helpdesk support</li></ul>
        </div>
      </article>
      <article class="panel">
        <div class="photo photo-cover" role="img" aria-label="Hand pressing a glowing button"></div>
        <svg class="swoosh" style="top:130px" width="182" height="60" viewBox="0 0 182 60" aria-hidden="true">
          <path d="M0 40 Q100 5 182 25 L182 60 L0 60Z" fill="#fff"/>
          <path d="M0 40 Q100 5 182 25" fill="none" stroke="#dfe6ee" stroke-width="4"/>
        </svg>
        <div class="cover-mark"><div class="mark-circle"></div><div class="cover-name">tulmori</div></div>
        <div class="web-bar">www.lorvex.net</div>
      </article>
    </div>

    <article class="flyer" style="--accent:var(--green)">
      <div class="flyer-logo"><span class="dot"></span><span>tulmori</span></div>
      <div class="photo photo-team" role="img" aria-label="Group of business people"></div>
      <svg class="swoosh" style="top:128px" width="134" height="40" viewBox="0 0 134 40" aria-hidden="true"><path d="M0 26 Q70 0 134 12 L134 40 L0 40Z" fill="#fff"/><path d="M0 24 Q70 -2 134 10" fill="none" stroke="#5fae3c" stroke-width="4"/></svg>
      <div class="section"><div class="label"><span class="dot"></span>tulmori services</div><p class="copy">We build secure networks, software and support services that help growing companies work faster every day.</p><ul class="bullets"><li>Managed servers and cloud hosting</li><li>Round the clock helpdesk support</li><li>Custom software for your team</li></ul></div>
      <div class="web-bar">www.lorvex.net</div>
    </article>
    <article class="flyer" style="--accent:var(--green)">
      <div class="flyer-logo"><span class="dot"></span><span>tulmori</span></div>
      <div class="photo photo-team" role="img" aria-label="Group of business people"></div>
      <svg class="swoosh" style="top:128px" width="134" height="40" viewBox="0 0 134 40" aria-hidden="true"><path d="M0 26 Q70 0 134 12 L134 40 L0 40Z" fill="#fff"/><path d="M0 24 Q70 -2 134 10" fill="none" stroke="#5fae3c" stroke-width="4"/></svg>
      <div class="section"><div class="label"><span class="dot"></span>tulmori services</div><p class="copy">We build secure networks, software and support services that help growing companies work faster every day.</p><ul class="bullets"><li>Managed servers and cloud hosting</li><li>Round the clock helpdesk support</li><li>Custom software for your team</li></ul></div>
      <div class="web-bar">www.lorvex.net</div>
    </article>
    <article class="flyer" style="--accent:var(--blue)">
      <div class="flyer-logo"><span class="dot"></span><span>tulmori</span></div>
      <div class="photo photo-team" role="img" aria-label="Business man at a desk"></div>
      <svg class="swoosh" style="top:128px" width="134" height="40" viewBox="0 0 134 40" aria-hidden="true"><path d="M0 26 Q70 0 134 12 L134 40 L0 40Z" fill="#fff"/><path d="M0 24 Q70 -2 134 10" fill="none" stroke="#2f7fc2" stroke-width="4"/></svg>
      <div class="section"><div class="label"><span class="dot"></span>tulmori solutions</div><p class="copy">We build secure networks, software and support services that help growing companies work faster every day.</p><ul class="bullets"><li>Managed servers and cloud hosting</li><li>Round the clock helpdesk support</li><li>Custom software for your team</li></ul></div>
      <div class="web-bar">www.lorvex.net</div>
    </article>
    <article class="flyer" style="--accent:var(--blue)">
      <div class="flyer-logo"><span class="dot"></span><span>tulmori</span></div>
      <div class="photo photo-team" role="img" aria-label="Two business people talking"></div>
      <svg class="swoosh" style="top:128px" width="134" height="40" viewBox="0 0 134 40" aria-hidden="true"><path d="M0 26 Q70 0 134 12 L134 40 L0 40Z" fill="#fff"/><path d="M0 24 Q70 -2 134 10" fill="none" stroke="#2f7fc2" stroke-width="4"/></svg>
      <div class="section"><div class="label"><span class="dot"></span>tulmori solutions</div><p class="copy">We build secure networks, software and support services that help growing companies work faster every day.</p><ul class="bullets"><li>Managed servers and cloud hosting</li><li>Round the clock helpdesk support</li><li>Custom software for your team</li></ul></div>
      <div class="web-bar">www.lorvex.net</div>
    </article>
  </section>

</main>
</body>
</html>
```